依頼詳細
◇サイトマップ
①Home
②MENU&PRICE
③SALON INFO
④PRODUCTS
⑤GALLERY ※一旦非表示
⑥STAFF(一覧・詳細)
⑦RECRUIT
⑧CONCEPT
⑨BLOG(一覧・詳細)
⑩NEWS(一覧・詳細)
⑪CONTACT
⑫CUT
⑬COLOR
⑭PERM
⑮TREATMENT
⑯STRAIGHT

◇優先事項
1.ユーザビリティー
2.編集更新
3.凝ったデザイン

◇期待する効果
1.新規顧客の獲得
2.売上の向上
3.イメージアップ

◇ターゲット
【性別】男女比(男 3:7 女)
【年代】30代~60代
【属性】会社員 自営業 主婦

◇素材について
写真データ(店舗内観・外観・人物・施術内容)

◇デザイン
シンプル(2) 複雑
単色  (3) カラフル
暗い  (3) 明るい
日常  (3) 高級
遊び心 (3) 厳粛
未来的 (3) 伝統的
女性  (3) 男性

◇テイスト
◯ ナチュラル 清潔感
× にぎやか 幻想的・神秘的 派手

◇希望カラー
差し色 (茶系やグレー系)
基本的にはお任せで構わない。

◇参考サイト
http://www.mirateki.jp/
見やすくてシンプルで良いが、殺風景すぎるかも・・

http://dovanpix.com/
かなり好きなデザイン。ただ狙っている客層がうちより若すぎるかもしれない。

http://www.sopravin-lab.net/
かっこいいさいとだが、ちょっとうちにはかっこよすぎて、合わないかも・・

http://www.tomsuriweb.com/
良いサイトだと思うが、写真の角などが尖っているのが好きではない。
希望イメージ
シンプル 複雑
単色 カラフル
暗い 明るい
日常 高級
遊び心 厳粛
未来的 伝統的
女性的 男性的
希望する色
茶系、グレー系、上記2色はいれて欲しいがその他は基本的にはお任せで構いません。
納品ファイル
• イラストレーター形式 (.ai)
• フォトショップ形式 (.psd)
• PNG形式 (.png)
補足説明
素材①
店内写真などをソラクモボックスを使って、アップしています。
下記URLよりダウンロードしてください。
■ダウンロード
URL:http://kumosoko.jp/download/a38204917652c14e7b3806df1a9358e62c40b7d2
ダウンロードパスワード pass

素材②
ピクセナ:https://jp.pixenaimg.com/
当社で定期契約をしています。クレジット購入のみのもの以外をご利用下さい。
また定期契約のものは弊社の負担となり、ランサー様に負担はありません。
カンプ画像を入れてください。

素材③
ポータルサイトの情報を元に作成をお願い致します。
http://mobirupa.jp/kansai/wakayama/41587/hair/5802-02104916-000/shop_top/
画像やテキストに関しては一旦引き抜いて頂いて構いません。

デザインが気に入ったため、選定させて頂きました。
修正もスムーズに進めて頂きました。

皆様、ありがとうございます!

```html
<!DOCTYPE html>
<html lang="ja">
<head>
<meta charset="utf-8">
<title>LUMERA hair salon</title>
<link href="https://fonts.googleapis.com/css2?family=Noto+Sans+JP:wght@400;500;700&family=Noto+Serif+JP:wght@500;700&family=Cormorant+Garamond:wght@600&display=swap" rel="stylesheet">
<style>
:root{
  --page-bg:#efefef;
  --paper:#ffffff;
  --brown:#a0733f;
  --brown-dark:#8a5f33;
  --brown-light:#d8c3a5;
  --text:#555555;
  --muted:#9a9a9a;
  --line:#e3e3e3;
  --footer-bg:#f4f3f1;
  --ink:#333333;
}
*{margin:0;padding:0;box-sizing:border-box}
html,body{width:1200px;height:3268px;overflow:hidden}
body{background:var(--page-bg);font-family:"Noto Sans JP",sans-serif;color:var(--text)}
.page{position:absolute;left:112px;top:0;width:976px;height:3268px;background:var(--paper)}
section,header,footer{position:relative;width:976px}

.site-header{height:112px}
.logo{position:absolute;left:32px;top:38px;font-family:"Cormorant Garamond",serif;font-weight:600;font-size:20px;letter-spacing:4px;color:var(--brown-dark)}
.nav{position:absolute;right:40px;top:44px;display:flex;gap:40px;list-style:none}
.nav li{position:relative;font-size:11px;letter-spacing:1.5px;color:var(--muted)}
.nav li.active{color:var(--brown)}
.nav li.active::before{content:"";position:absolute;left:50%;top:-12px;width:4px;height:4px;margin-left:-2px;border-radius:50%;background:var(--brown)}

.hero{height:648px}
.hero-photo{position:absolute;inset:0;background:linear-gradient(100deg,#cfc3b3 0%,#b9a78f 35%,#e4dbcf 60%,#f3eee6 100%)}
.slider-arrow{position:absolute;top:312px;width:24px;height:24px}
.slider-arrow.prev{left:16px}
.slider-arrow.next{right:16px}

.concept{height:728px}
.concept h2{position:absolute;top:76px;width:100%;text-align:center;font-family:"Noto Serif JP",serif;font-weight:700;font-size:20px;letter-spacing:3px;color:var(--brown)}
.concept .lead{position:absolute;top:120px;width:100%;text-align:center;font-size:13px;line-height:28px;color:var(--text)}
.feature-main{position:absolute;left:80px;top:264px;width:468px;height:320px;background:linear-gradient(135deg,#d9cbb7,#a98d6c 60%,#6f5a44)}
.feature-main p{position:absolute;left:28px;bottom:26px;width:300px;font-size:13px;line-height:24px;color:#fff}
.feature-item{position:absolute;left:568px;width:340px;height:80px}
.feature-item .thumb{position:absolute;left:0;top:0;width:128px;height:80px}
.feature-item h3{position:absolute;left:140px;top:4px;width:200px;font-size:13px;font-weight:500;line-height:22px;color:var(--ink)}
.feature-item time{position:absolute;left:140px;top:52px;font-size:10px;color:var(--muted)}

.lovely-band{height:312px;background:linear-gradient(180deg,#9c7244 0%,#b58e63 55%,#e1cdb4 100%)}
.lovely-btn{position:absolute;left:348px;top:116px;width:280px;height:72px;border:2px solid #fff;color:#fff;font-size:14px;font-weight:500;letter-spacing:2px;display:flex;align-items:center;justify-content:center}

.staff{height:800px}
.staff h2{position:absolute;top:112px;width:100%;text-align:center;font-family:"Noto Serif JP",serif;font-weight:700;font-size:24px;letter-spacing:4px;color:var(--brown)}
.staff h2::after{content:"";position:absolute;left:50%;top:44px;width:40px;height:2px;margin-left:-20px;background:var(--brown-light)}
.staff-photo{position:absolute;top:248px;height:344px}
.staff-arrow{position:absolute;top:402px;width:24px;height:24px}

.site-footer{height:500px;background:var(--footer-bg)}
.site-footer h4{position:absolute;top:54px;font-size:12px;font-weight:700;letter-spacing:1.5px;color:var(--brown)}
.access-h{left:160px}
.info-h{left:656px}
.access-addr{position:absolute;left:160px;top:96px;font-size:11px;color:var(--text)}
.map{position:absolute;left:160px;top:136px;width:440px;height:288px;background:linear-gradient(135deg,#e9ebe6,#dde2dc 50%,#e6e3dc)}
.info-list{position:absolute;left:656px;top:92px;list-style:none;font-size:11px;line-height:24px;color:var(--text)}

.bottom{height:168px}
.copyright{position:absolute;top:56px;width:100%;text-align:center;font-size:10px;color:var(--muted)}
.social{position:absolute;top:94px;left:0;width:100%;display:flex;justify-content:center;gap:20px;list-style:none}
.social li{width:22px;height:22px;border-radius:50%;background:var(--ink)}
</style>
</head>
<body>
<div class="page">
  <header class="site-header">
    <div class="logo">LUMERA</div>
    <ul class="nav">
      <li class="active">HOME</li>
      <li>STAFF</li>
      <li>BLOG</li>
      <li>NEWS</li>
      <li>CONTACT</li>
    </ul>
  </header>

  <section class="hero">
    <div class="hero-photo" role="img" aria-label="Salon reception counter with stone wall and wooden shelf"></div>
    <svg class="slider-arrow prev" viewBox="0 0 24 24"><path d="M15 4 7 12l8 8" fill="none" stroke="#fff" stroke-width="2"/></svg>
    <svg class="slider-arrow next" viewBox="0 0 24 24"><path d="M9 4l8 8-8 8" fill="none" stroke="#fff" stroke-width="2"/></svg>
  </section>

  <section class="concept">
    <h2>寛げる空間を</h2>
    <p class="lead">ウッドテイストで落ち着きのある空間<br>半個室での施術により更にリラックス</p>
    <div class="feature-main" role="img" aria-label="Semi-private styling booth with chair and mirror">
      <p>半個室での施術により、周りを気にせずゆったりお過ごし頂けます</p>
    </div>
    <article class="feature-item" style="top:264px">
      <div class="thumb" role="img" aria-label="Styling seats for groups" style="background:linear-gradient(135deg,#c9b296,#8f7457)"></div>
      <h3>家族や友人同士でご来店の際</h3>
      <time>2017.06.01</time>
    </article>
    <article class="feature-item" style="top:376px">
      <div class="thumb" role="img" aria-label="Relaxed waiting area" style="background:linear-gradient(135deg,#e2d6c6,#a88d70)"></div>
      <h3>落ち着くゆったりとした<br>待合スペース</h3>
      <time>2017.06.01</time>
    </article>
  </section>

  <section class="lovely-band">
    <div class="lovely-btn">FOR YOUR LOVELY DAY</div>
  </section>

  <section class="staff">
    <h2>STAFF</h2>
    <svg class="staff-arrow" style="left:56px" viewBox="0 0 24 24"><path d="M15 5 8 12l7 7" fill="none" stroke="#666" stroke-width="2"/></svg>
    <div class="staff-photo" role="img" aria-label="Stylist portrait, man in dark jacket" style="left:88px;width:232px;background:linear-gradient(180deg,#f3f3f3,#cfcfcf 50%,#3d3d42)"></div>
    <div class="staff-photo" role="img" aria-label="Stylist portrait, woman with flower" style="left:356px;width:264px;background:linear-gradient(180deg,#f7eef2,#efc9d0 50%,#f4dfe4)"></div>
    <div class="staff-photo" role="img" aria-label="Stylist portrait, woman in light cardigan" style="left:648px;width:240px;background:linear-gradient(180deg,#fafafa,#d8d3d3 50%,#aeb4c4)"></div>
    <svg class="staff-arrow" style="left:896px" viewBox="0 0 24 24"><path d="M9 5l7 7-7 7" fill="none" stroke="#666" stroke-width="2"/></svg>
  </section>

  <footer class="site-footer">
    <h4 class="access-h">ACCESS</h4>
    <p class="access-addr">和歌山県和歌山市 架空町1-2-3 ハナミズキビル2F</p>
    <div class="map" role="img" aria-label="Map showing salon location"></div>
    <h4 class="info-h">INFO</h4>
    <ul class="info-list">
      <li>TEL 073-000-1234</li>
      <li>営業時間 9:00〜19:00</li>
      <li>定休日 月曜日・第1・第3火曜日</li>
    </ul>
  </footer>

  <section class="bottom">
    <p class="copyright">Copyright © LUMERA hair salon 和歌山県和歌山市 All Rights Reserved.</p>
    <ul class="social">
      <li aria-label="social link"></li>
      <li aria-label="social link"></li>
      <li aria-label="social link"></li>
    </ul>
  </section>
</div>
</body>
</html>
```